Beauty Salon Design

The business card design will be for a new beauty salon opening up.

The therapist has over 11 years at a leading beauty Salon in perth.

The two colours that the salon will use is black and gold.

Industry/Entity Type

Beauty Salon

Contact Information for Business Card

Lumora Beauty

Corinne Halstead Pryce
Advanced beauty therapist
0455 817 302

Monday - Friday 9am - 2.30pm
Weekends and nights by appointment only

Waxing, Tinting, Swedish massage, hot stone massage, facials, peels, micro, LED light treatment, skin needling and retail products.

```html
<!DOCTYPE html>
<html lang="en">
<head>
<meta charset="utf-8">
<title>Lumora Beauty – Business Card</title>
<link rel="stylesheet" href="https://fonts.googleapis.com/css2?family=EB+Garamond:wght@500;600;700&display=swap">
<style>
  :root {
    --page: #d9dee0;
    --card-black: #0b0b0b;
    --card-charcoal: #262423;
    --band-grey: #302f2f;
    --gold: #d9c21e;
    --gold-deep: #a8890f;
    --gold-light: #f3e37a;
    --text-light: #ffffff;
    --art-dark: #1e1b18;
    --art-warm: #6d5f4a;
  }
  * { margin: 0; padding: 0; box-sizing: border-box; }
  html, body {
    width: 1200px; height: 900px; overflow: hidden;
    background: var(--page);
    font-family: "EB Garamond", Georgia, serif;
  }
  .sheet { position: relative; width: 1200px; height: 900px; }
  .card {
    position: absolute; left: 240px; width: 720px; height: 410px;
    overflow: hidden; box-shadow: 0 6px 18px rgba(0,0,0,.25);
  }

  /* ---------- Back: hours and services ---------- */
  .card-back {
    top: 30px;
    background: linear-gradient(180deg, var(--card-charcoal) 0%, #1c1a19 55%, #121111 100%);
  }
  .hours-band {
    position: absolute; inset: 0 0 auto 0; height: 100px;
    background: var(--band-grey);
    text-align: center; color: var(--text-light);
    padding-top: 14px; padding-left: 60px;
  }
  .hours-main { font-size: 34px; font-weight: 600; line-height: 1.1; }
  .hours-note { font-size: 21px; font-weight: 600; margin-top: 4px; }
  .portrait-art {
    position: absolute; right: 0; top: 100px; width: 330px; height: 250px;
    background: radial-gradient(ellipse at 60% 40%, var(--art-warm) 0%, #3f3729 40%, var(--art-dark) 80%);
  }
  .service-list {
    position: absolute; left: 34px; top: 124px;
    list-style: none; color: var(--text-light);
    font-size: 25px; font-weight: 700; line-height: 36px;
  }
  .gold-flourish {
    position: absolute; left: 0; right: 0; bottom: 22px; height: 26px;
    background: linear-gradient(90deg, var(--gold-deep) 0%, var(--gold-light) 55%, var(--gold) 100%);
  }

  /* ---------- Front: name and contact ---------- */
  .card-front { top: 470px; background: var(--card-black); }
  .mask-photo {
    position: absolute; left: 0; top: 50px; width: 360px; height: 270px;
    background: radial-gradient(ellipse at 50% 50%, #b9ad8e 0%, #7d7360 35%, #2c2925 70%, var(--card-black) 100%);
  }
  .brand-name {
    position: absolute; right: 60px; top: 22px;
    color: var(--gold); font-size: 54px; font-weight: 600; letter-spacing: 1px;
  }
  .brand-flourish {
    position: absolute; right: 20px; top: 112px; width: 360px; height: 16px;
    background: linear-gradient(90deg, var(--gold-deep) 0%, var(--gold-light) 60%, var(--gold) 100%);
  }
  .contact {
    position: absolute; right: 36px; top: 200px; text-align: right;
    color: var(--text-light);
  }
  .contact-name { font-size: 30px; font-weight: 700; letter-spacing: .5px; }
  .contact-role { font-size: 23px; font-weight: 600; margin-top: 2px; }
  .contact-phone { font-size: 23px; font-weight: 600; letter-spacing: 1.5px; margin-top: 2px; }
</style>
</head>
<body>
<main class="sheet">

  <section class="card card-back">
    <div class="portrait-art" role="img" aria-label="Illustration of a woman's silhouette with ornate floral swirls"></div>
    <header class="hours-band">
      <p class="hours-main">Monday - Friday 9am - 2.30pm</p>
      <p class="hours-note">Weekends and nights by appointment only</p>
    </header>
    <ul class="service-list">
      <li>Waxing, Tinting,</li>
      <li>Swedish massage,</li>
      <li>Hot stone massage,</li>
      <li>Facials, Peels,</li>
      <li>Micro, LED light treatment,</li>
      <li>Skin needling &amp; Retail products.</li>
    </ul>
    <div class="gold-flourish" role="img" aria-label="Gold wave ornament"></div>
  </section>

  <section class="card card-front">
    <div class="mask-photo" role="img" aria-label="Photograph of an ornate gold and silver masquerade mask"></div>
    <h1 class="brand-name">Lumora Beauty</h1>
    <div class="brand-flourish" role="img" aria-label="Gold wave ornament"></div>
    <div class="contact">
      <p class="contact-name">Corinne Halstead Pryce</p>
      <p class="contact-role">Advanced beauty therapist</p>
      <p class="contact-phone">T: 0455 817 302</p>
    </div>
  </section>

</main>
</body>
</html>
```